Simple Modern Label for a Coconut oil product

We need a label designed for Organic Coconut oil. We would like the label to convey the gourmet/high quality product. It should be modern and simple and look like an artisinal product. The label will need to contain all the basic label requirements - Independence list, place for nutrition facts, our company logo etc.
The label will ultimately be printed as oil proof, so it will have a glossy appearance.
I have includes some examples that I like and a file with the logo.

Product Container - Wide Mount Clear Glass Jar: 4.75 inches tall (base to the bottom of the lid) and 9.5 in circumference
Label: Can be 1 or 2 separate labels, round, square and rectangle are okay
No larger than 3 inches high and 9 inches long

Target Market(s)

Middle Age home chef

Industry/Entity Type

Product

Requirements
Must have
• - logo (Attached below, I have this in multiple formats, let me know if you need them)
• - 14 FL OZ (414mL)
• - ingredient: organic unrefined whole kernel virgin coconut oil,
• - Manufacturer: XXX Y St., anywhere, CA, 99999
• - Distributed by Fernvale Naturals, P.O. Box 5521, Oakland, CA 94610 www.FernvaleNaturals.example
• - Certified Organic by Company Name
• - Product of Sri Lanka
Nice to have
• - Nutrition Facts
Should not have
• Clutter

```html
<!DOCTYPE html>
<html lang="en">
<head>
<meta charset="utf-8">
<title>Fernvale Naturals — Coconut Oil Label</title>
<link rel="stylesheet" href="https://fonts.googleapis.com/css2?family=Questrial&family=Arimo:wght@700&family=Cabin:wght@400&display=swap">
<style>
  :root {
    --bg: #96feb8;
    --oil: #f2f0b5;
    --glass: #f4fbf6;
    --label: #ffffff;
    --cap: #1e1e1e;
    --cork: #c09a5b;
    --ink: #2b2b2b;
    --tan: #c09a5b;
    --brown: #6b3f1d;
    --copy: #4a4a3a;
  }
  html, body { margin: 0; padding: 0; overflow: hidden; }
  .canvas {
    position: relative;
    width: 1200px; height: 1200px;
    background: var(--bg);
    overflow: hidden;
  }
  .bottles { position: absolute; inset: 0; }
  .name {
    position: absolute;
    font-family: "Questrial", sans-serif;
    color: var(--ink);
    text-align: center;
    line-height: 1;
    margin: 0;
    letter-spacing: 0.02em;
  }
  .descriptor {
    position: absolute;
    font-family: "Arimo", sans-serif;
    font-weight: 700;
    color: var(--tan);
    text-align: center;
    margin: 0;
    line-height: 1;
  }
  .brand-mark .name { left: 870px; width: 330px; font-size: 44px; }
  .brand-mark .name-line1 { top: 180px; }
  .brand-mark .name-line2 { top: 236px; }
  .brand-mark .descriptor { left: 870px; width: 330px; top: 290px; font-size: 30px; }

  .front-label .name { left: 264px; width: 186px; font-size: 26px; }
  .front-label .name-line1 { top: 498px; }
  .front-label .name-line2 { top: 533px; }
  .front-label .descriptor { left: 264px; width: 186px; top: 568px; font-size: 20px; }
  .front-label .volume {
    position: absolute; right: 754px; top: 624px;
    font-family: "Questrial", sans-serif; font-size: 18px; color: var(--ink);
    margin: 0; line-height: 1;
  }

  .back-label {
    position: absolute; left: 667px; top: 432px; width: 176px;
    font-family: "Cabin", sans-serif; font-size: 14px; line-height: 19px;
    color: var(--copy);
  }
  .back-label p { margin: 0 0 19px; }
  .back-label .web { font-size: 11.5px; line-height: 14px; display: block; }
</style>
</head>
<body>
<main class="canvas">
  <svg class="bottles" width="1200" height="1200" viewBox="0 0 1200 1200" aria-hidden="true">
    <g class="bottle bottle-front">
      <rect x="316" y="180" width="83" height="88" fill="var(--glass)"/>
      <rect x="315" y="157" width="84" height="25" rx="2" fill="var(--cap)"/>
      <polygon points="317,182 397,182 393,206 375,228 339,228 321,206" fill="var(--cork)"/>
      <rect x="258" y="262" width="198" height="824" rx="16" fill="var(--glass)"/>
      <rect x="265" y="268" width="184" height="812" rx="11" fill="var(--oil)"/>
      <rect x="258" y="402" width="198" height="248" fill="var(--label)"/>
      <circle cx="362" cy="450" r="26" fill="var(--brown)"/>
    </g>
    <g class="bottle bottle-back">
      <rect x="706" y="180" width="83" height="88" fill="var(--glass)"/>
      <rect x="705" y="157" width="84" height="25" rx="2" fill="var(--cap)"/>
      <polygon points="707,182 787,182 783,206 765,228 729,228 711,206" fill="var(--cork)"/>
      <rect x="648" y="262" width="198" height="824" rx="16" fill="var(--glass)"/>
      <rect x="655" y="268" width="184" height="812" rx="11" fill="var(--oil)"/>
      <rect x="648" y="402" width="198" height="362" fill="var(--label)"/>
    </g>
    <circle class="brand-dot" cx="1036" cy="96" r="72" fill="var(--brown)"/>
  </svg>

  <section class="brand-mark">
    <p class="name name-line1">FERNVALE</p>
    <p class="name name-line2">NATURALS</p>
    <p class="descriptor">coconut oil</p>
  </section>

  <section class="front-label">
    <p class="name name-line1">FERNVALE</p>
    <p class="name name-line2">NATURALS</p>
    <p class="descriptor">coconut oil</p>
    <p class="volume">14 FL OZ</p>
  </section>

  <section class="back-label">
    <p>Ingredient: organic unrefined whole kernel virgin coconut oil</p>
    <p>manufacturer: XXX Y st., anywhere, CA, 99999</p>
    <p>Distributed by Fernvale Naturals, P.O. Box 5521, Oakland, CA 94610 <span class="web">www.FernvaleNaturals.example</span></p>
    <p>Certified organic by Harborline Certifiers</p>
    <p>Product of Sri Lanka</p>
  </section>
</main>
</body>
</html>
```